Corvane Partners Web Design

Dear all
I need a web design for a financial services site. We are a broker who deals with many different financial institutions and require a clean, simple and instantly impressive site based on the colour scheme that SketchGuild created for us. A landing page (www.crvnp.mx) gives an idea of the logo and clour scheme but we are looking at either a one page site with rollover text boxes or a 3 or 4 page site depending on the preference of the designer and the best user experience. The site“s purpose is to give confidence that the company exists rather than impart pages of information although we would like this to be a site that can expand over time as the company grows. For now the requirement is for a clear set of possibly changing images at the centre of a white screen that relate to finance in general nad the benefits of wealth creation as well as sectios either along the top or bottom - Our Company, Our Approach, Our services, Our clients, Contact (user to fill in contact box to be sent to info@crvnp.mx. The text for each of these boxes I assume can be added by the coding team here, it the overall look and feel that I am looking for from SketchGuild - deadline can be extended if necessary but I was hoping to wrap this all up in October

Target Market(s)

Succesful individuals looking to maximise returns on their investment via world class financial institutions and supported throughout by qualified independent financial advisors

Industry/Entity Type

Finance

Requirements
Must have
• Logo and color scheme of the logo design SketchGuild sent - I have all these sourcefiles, pantone and fonts

```html
<!DOCTYPE html>
<html lang="en">
<head>
<meta charset="utf-8">
<title>Corvane Partners</title>
<link rel="stylesheet" href="https://fonts.googleapis.com/css2?family=Arimo:wght@400;700&display=swap">
<style>
:root{
  --navy:#1e3a66;
  --navy-deep:#162d52;
  --orange:#f5a020;
  --grey-icon:#8b8b8b;
  --text:#666a70;
  --light:#f6f6f6;
  --white:#ffffff;
}
*{box-sizing:border-box;margin:0;padding:0}
html,body{width:1200px;height:2284px;overflow:hidden}
body{font-family:"Arimo",Arial,sans-serif;color:var(--text);background:var(--white);position:relative}
a{color:inherit;text-decoration:none}
.abs{position:absolute}

/* top bar */
.topbar{left:0;top:0;width:1200px;height:52px;background:var(--navy);color:#dfe6f1;font-size:12px}
.account-links{left:110px;top:19px;letter-spacing:.2px}
.account-links span{margin:0 8px}
.main-nav{right:107px;top:20px;display:flex;gap:33px;font-size:11.5px;text-transform:uppercase}
.main-nav .active{color:var(--orange)}

/* hero */
.hero{left:0;top:52px;width:1200px;height:548px;background:linear-gradient(100deg,#c9ccd1 0%,#e8e9ea 35%,#f3f3f3 55%,#c8ccd2 80%,#9aa2ad 100%)}
.brand{left:106px;top:120px;display:flex;align-items:center;gap:14px}
.brand-mark{width:30px;height:30px;border-radius:50%;background:var(--navy)}
.brand-name{font-size:30px;color:var(--navy);letter-spacing:1px}
.hero-caption{left:108px;top:379px;width:436px;height:134px;background:rgba(30,58,102,.92);color:var(--white);padding:34px 42px}
.hero-caption h1{font-size:22px;font-weight:400;line-height:31px}
.hero-caption .more{position:absolute;right:44px;bottom:24px;font-size:12px}
.slide-btn{top:528px;width:52px;height:52px;display:flex;align-items:center;justify-content:center}
.slide-prev{left:108px;background:var(--orange)}
.slide-next{left:168px;background:var(--navy)}

/* about */
.section-title{width:1200px;text-align:center;font-size:25px;color:var(--navy);font-weight:400}
.section-title em{font-style:normal;color:var(--orange)}
.about-text{left:128px;top:760px;width:956px;text-align:center;font-size:13px;line-height:24px}

/* services */
.services{left:0;top:900px;width:1200px;height:455px;background:var(--light)}
.service{width:170px;text-align:center}
.service-icon{width:116px;height:116px;border-radius:50%;background:var(--navy);margin:0 auto;display:flex;align-items:center;justify-content:center}
.service-icon.muted{background:var(--grey-icon)}
.service-label{margin-top:22px;font-size:13.5px;color:var(--navy)}
.cta{top:335px;height:48px;display:flex;align-items:center;color:var(--white);font-size:13px;text-transform:uppercase}
.cta-why{left:372px;width:214px;background:var(--navy)}
.cta-calc{left:611px;width:215px;background:var(--orange)}
.cta svg{margin:0 22px 0 14px}

/* news */
.news{left:0;top:1355px;width:1200px;height:565px;background:#f9f9f9}
.news-item{left:108px;width:430px;height:82px}
.date-box{width:89px;height:81px;background:var(--navy);color:var(--white);text-align:center;padding-top:17px}
.date-box b{display:block;color:var(--orange);font-size:20px}
.date-box span{display:block;font-size:14px;margin-top:10px}
.news-title{left:114px;top:6px;font-size:17px;color:var(--navy)}
.news-text{left:114px;top:44px;width:310px;font-size:12.5px;line-height:20px}
.testimonial{left:666px;width:426px;height:82px}
.avatar{width:83px;height:73px;background:linear-gradient(135deg,#c9b8a6,#6f6a66)}
.quote{left:112px;top:-4px;width:312px;font-size:12.5px;line-height:20px}
.quote-author{right:2px;top:69px;font-size:12px;color:var(--navy)}
.view-all{top:1858px;font-size:13px;color:var(--navy)}

/* footer */
.footer{left:0;top:1920px;width:1200px;height:320px;background:var(--navy);color:var(--white)}
.footer h3{font-size:16px;font-weight:400;color:var(--orange);margin-bottom:22px}
.footer-col{top:48px;font-size:12.5px;line-height:23.5px}
.footer ul{list-style:none}
.contact-row{display:flex}
.contact-row span:first-child{width:50px}
.footer .mail-title{margin:14px 0 6px}
.copybar{left:0;top:2240px;width:1200px;height:44px;background:var(--navy-deep);color:var(--white);font-size:12.5px}
.copyright{left:108px;top:15px}
.follow{left:893px;top:8px;display:flex;align-items:center;gap:8px}
.follow span{margin-right:10px}
.social{width:32px;height:32px;border-radius:4px;background:#4a6fb0}
.social.alt{background:#3c9bd6}
.social.third{background:#6d8fc4}
</style>
</head>
<body>

<header class="abs topbar">
  <div class="abs account-links"><a href="#">Help Desk</a><span>|</span><a href="#">Sign in</a><span>|</span><a href="#">Register</a></div>
  <nav class="abs main-nav">
    <a class="active" href="#">Home</a><a href="#">Investment</a><a href="#">About us</a><a href="#">Services</a><a href="#">Onlie calculator</a><a href="#">News &amp; Blog</a><a href="#">Contact us</a>
  </nav>
</header>

<section class="abs hero" role="img" aria-label="Office team working at computers, a smiling advisor with a headset in front">
  <div class="abs brand" style="top:68px">
    <div class="brand-mark"></div>
    <div class="brand-name">Corvane Partners</div>
  </div>
  <div class="abs hero-caption" style="top:327px">
    <h1>Creating your success through Financial Planning</h1>
    <a class="more" href="#">Learn more &gt;&gt;</a>
  </div>
  <a class="abs slide-btn slide-prev" style="top:476px" href="#"><svg width="12" height="20" viewBox="0 0 12 20"><path d="M10 2 2 10l8 8" fill="none" stroke="#fff" stroke-width="2"/></svg></a>
  <a class="abs slide-btn slide-next" style="top:476px" href="#"><svg width="12" height="20" viewBox="0 0 12 20"><path d="M2 2l8 8-8 8" fill="none" stroke="#fff" stroke-width="2"/></svg></a>
</section>

<h2 class="abs section-title" style="top:694px">Something about <em>Corvane Financial Group</em></h2>
<p class="abs about-text">Lorem Ipsum is simply dummy text of the printing and typesetting industry. Lorem Ipsum has been the industry's standard dummy text ever since the 1500s, when an unknown printer took a galley of type and scrambled it to make a type specimen book. It has survived not only five centuries, but also the leap into electronic typesetting, remaining essentially unchanged. It was popularised in the 1960s with the release of Letraset sheets containing Lorem Ipsum passages, and more recently with desktop publishing software like Aldus PageMaker including versions of Lorem Ipsum.</p>

<section class="abs services">
  <h2 class="abs section-title" style="top:44px">Services We Are Providing</h2>
  <div class="abs service" style="left:118px;top:116px">
    <div class="service-icon muted"><svg width="50" height="40" viewBox="0 0 50 40"><rect x="2" y="9" width="46" height="29" rx="3" fill="#fff"/><path d="M17 9V4h16v5" fill="none" stroke="#fff" stroke-width="3"/><rect x="22" y="19" width="6" height="5" fill="#8b8b8b"/></svg></div>
    <div class="service-label">Investment</div>
  </div>
  <div class="abs service" style="left:317px;top:116px">
    <div class="service-icon"><svg width="50" height="50" viewBox="0 0 50 50"><path d="M3 24a22 20 0 0 1 44 0z" fill="#fff"/><path d="M25 24v16a4 4 0 0 1-8 0" fill="none" stroke="#fff" stroke-width="3"/></svg></div>
    <div class="service-label">Life Insurance</div>
  </div>
  <div class="abs service" style="left:517px;top:116px">
    <div class="service-icon"><svg width="56" height="46" viewBox="0 0 56 46"><g fill="#fff"><rect x="22" y="4" width="32" height="5"/><rect x="22" y="12" width="32" height="5"/><rect x="22" y="20" width="32" height="5"/><rect x="22" y="28" width="32" height="5"/><rect x="22" y="36" width="32" height="5"/><circle cx="16" cy="26" r="15"/></g><text x="16" y="32" text-anchor="middle" font-family="Arimo,Arial,sans-serif" font-size="17" font-weight="700" fill="#1e3a66">$</text></svg></div>
    <div class="service-label">Income protection</div>
  </div>
  <div class="abs service" style="left:716px;top:116px">
    <div class="service-icon"><svg width="50" height="44" viewBox="0 0 50 44"><path d="M25 2 2 22h7v20h12V30h8v12h12V22h7z" fill="#fff"/></svg></div>
    <div class="service-label">Mortgage protection</div>
  </div>
  <div class="abs service" style="left:913px;top:116px">
    <div class="service-icon"><svg width="48" height="48" viewBox="0 0 48 48"><path d="M30 8H6v34h34V20" fill="none" stroke="#fff" stroke-width="4"/><path d="M40 4l5 5-19 19-8 3 3-8z" fill="#fff"/></svg></div>
    <div class="service-label">Pensions</div>
  </div>
  <a class="abs cta cta-why" href="#"><svg width="24" height="24" viewBox="0 0 24 24"><rect width="24" height="24" rx="3" fill="#31568f"/><circle cx="9" cy="9" r="3" fill="#fff"/><circle cx="15" cy="10" r="3" fill="#fff"/><path d="M4 19c0-4 3-6 5-6s5 2 5 6zM11 19c0-4 2-6 4-6s5 2 5 6z" fill="#fff"/></svg>Why choose Corvane</a>
  <a class="abs cta cta-calc" href="#"><svg width="20" height="24" viewBox="0 0 20 24"><rect x="1" y="1" width="18" height="22" rx="2" fill="none" stroke="#fff" stroke-width="2"/><rect x="4" y="4" width="12" height="5" fill="#fff"/><g fill="#fff"><rect x="4" y="12" width="3" height="3"/><rect x="9" y="12" width="3" height="3"/><rect x="14" y="12" width="2" height="3"/><rect x="4" y="17" width="3" height="3"/><rect x="9" y="17" width="3" height="3"/><rect x="14" y="17" width="2" height="3"/></g></svg><span style="margin-left:24px">Online calucator</span></a>
</section>

<section class="abs news">
  <h2 class="abs section-title" style="top:42px">Latest News and Testimonials</h2>

  <article class="abs news-item" style="top:112px">
    <div class="date-box"><b>OCT 22</b><span>2013</span></div>
    <h3 class="abs news-title" style="font-weight:400">News Headline Goes Here</h3>
    <p class="abs news-text">Lorem Ipsum is simply dummy text of the printing and typesetting industry. Lorem Ipsum has</p>
  </article>
  <article class="abs news-item" style="top:247px">
    <div class="date-box"><b>OCT 22</b><span>2013</span></div>
    <h3 class="abs news-title" style="font-weight:400">News Headline Goes Here</h3>
    <p class="abs news-text">Lorem Ipsum is simply dummy text of the printing and typesetting industry. Lorem Ipsum has</p>
  </article>
  <article class="abs news-item" style="top:381px">
    <div class="date-box"><b>OCT 22</b><span>2013</span></div>
    <h3 class="abs news-title" style="font-weight:400">News Headline Goes Here</h3>
    <p class="abs news-text">Lorem Ipsum is simply dummy text of the printing and typesetting industry. Lorem Ipsum has</p>
  </article>

  <article class="abs testimonial" style="top:116px">
    <div class="avatar" role="img" aria-label="Portrait photo of the client"></div>
    <p class="abs quote">Lorem Ipsum is simply dummy text of the printing and typesetting industry. Lorem Ipsum has been the industry's standard dummy text ever since the 1500s, when</p>
    <div class="abs quote-author">Miss Rowan ( CEO of Company Name )</div>
  </article>
  <article class="abs testimonial" style="top:251px">
    <div class="avatar" role="img" aria-label="Portrait photo of the client" style="background:linear-gradient(135deg,#d8d8d8,#7a7a7a)"></div>
    <p class="abs quote">Lorem Ipsum is simply dummy text of the printing and typesetting industry. Lorem Ipsum has been the industry's standard dummy text ever since the 1500s, when</p>
    <div class="abs quote-author">Mr. Halden ( CEO of Company Name )</div>
  </article>
  <article class="abs testimonial" style="top:385px">
    <div class="avatar" role="img" aria-label="Portrait photo of the client" style="background:linear-gradient(135deg,#b8977c,#4b4340)"></div>
    <p class="abs quote">Lorem Ipsum is simply dummy text of the printing and typesetting industry. Lorem Ipsum has been the industry's standard dummy text ever since the 1500s, when</p>
    <div class="abs quote-author">Mr. Ossian ( CEO of Company Name )</div>
  </article>

  <a class="abs view-all" style="left:222px;top:503px" href="#">View All &nbsp;&gt;&gt;</a>
  <a class="abs view-all" style="left:778px;top:503px" href="#">View All &nbsp;&gt;&gt;</a>
</section>

<footer class="abs footer">
  <div class="abs footer-col" style="left:108px">
    <h3>Quick Links</h3>
    <ul><li>Home</li><li>About us</li><li>Services</li><li>Technology</li><li>News and Blog</li><li>Contact us</li><li>Privacy lokicy</li><li>Terms of Use</li></ul>
  </div>
  <div class="abs footer-col" style="left:362px">
    <h3>How can we help</h3>
    <ul><li>Buying a home</li><li>Refinancing</li><li>Investing</li><li>First Home Buyers</li><li>Commercial Finance</li><li>Veltra Property</li></ul>
  </div>
  <div class="abs footer-col" style="left:621px">
    <h3>Online calculators</h3>
    <ul><li>Loan Options Calculator</li><li>Split Loan Calculator</li><li>Extra Repayment Calculator</li><li>Borrowing Power Calculator</li><li>Stamp Duty Calculator</li><li>Budget Planner</li></ul>
  </div>
  <div class="abs footer-col" style="left:877px">
    <h3>Contact us</h3>
    <div class="contact-row"><span>PH. NO</span><span>: 000-0000-000</span></div>
    <div class="contact-row"><span>Email</span><span>: info@crvnp.mx</span></div>
    <div class="contact-row"><span>Fax</span><span>: info@crvnp.mx</span></div>
    <h3 class="mail-title">Mailing Address :</h3>
    <div>Company Mailling Address<br>Goes Here :</div>
  </div>
</footer>

<div class="abs copybar">
  <div class="abs copyright">Copyright © 2013 Kelvra.com</div>
  <div class="abs follow"><span>FOLLOW US :</span><a class="social" href="#" aria-label="Social profile one"></a><a class="social alt" href="#" aria-label="Social profile two"></a><a class="social third" href="#" aria-label="Social profile three"></a></div>
</div>

</body>
</html>
```